Cool way of displaying products for fashion store

We need a "product card" designed (i.e a standard way of displaying our fashion items). Please see attached PDF for further more details including a rough design we have done.

Target Market(s)

Streetwear

```html
<!DOCTYPE html>
<html lang="en">
<head>
<meta charset="utf-8">
<title>Product Card – Boombox Master</title>
<link href="https://fonts.googleapis.com/css2?family=Cinzel:wght@900&family=Fjalla+One&family=Poppins:wght@500&display=swap" rel="stylesheet">
<style>
  :root {
    --page-bg: #e6e6e6;
    --card-red: #fe2a47;
    --card-rim: #ff5a70;
    --panel-dark: #262626;
    --white: #ffffff;
    --ink: #1d1d1d;
    --chip-blue: #4f8fe8;
    --ring-orange: #f08a24;
    --price-grey: #a8a8a8;
    --btn-yellow: #f8d85c;
    --btn-orange: #eca45c;
  }
  * { margin: 0; padding: 0; box-sizing: border-box; }
  html, body { width: 960px; height: 1200px; overflow: hidden; background: var(--page-bg); }
  .canvas { position: relative; width: 960px; height: 1200px; }
  .card-art { position: absolute; inset: 0; }
  .rarity-label {
    position: absolute; left: 186px; top: 268px;
    font-family: "Poppins", sans-serif; font-weight: 500; font-size: 44px;
    color: var(--white); line-height: 1;
  }
  .rank-label {
    position: absolute; left: 597px; top: 217px;
    font-family: "Fjalla One", sans-serif; font-size: 17px; color: var(--white);
    line-height: 1;
  }
  .timer-label {
    position: absolute; left: 766px; top: 218px; width: 58px; text-align: center;
    font-family: "Fjalla One", sans-serif; font-size: 22px; color: var(--white); line-height: 1;
  }
  .product-name {
    position: absolute; left: 0; width: 990px; top: 818px; text-align: center;
    font-family: "Cinzel", serif; font-weight: 900; font-size: 46px; letter-spacing: 1px;
    color: var(--card-red); line-height: 1;
    -webkit-text-stroke: 3px var(--white); paint-order: stroke fill;
  }
  .price-value {
    position: absolute; left: 463px; top: 886px;
    font-family: "Fjalla One", sans-serif; font-size: 31px; color: var(--ink);
    letter-spacing: 1px; line-height: 1;
  }
  .view-label {
    position: absolute; left: 378px; width: 202px; top: 940px; text-align: center;
    font-family: "Fjalla One", sans-serif; font-size: 36px; color: var(--ink); line-height: 1.3;
  }
</style>
</head>
<body>
<main class="canvas">
  <svg class="card-art" width="960" height="1200" viewBox="0 0 1200 1500" xmlns="http://www.w3.org/2000/svg">
    <defs>
      <linearGradient id="ribbon-fill" x1="0" x2="1">
        <stop offset="0" stop-color="#b8142c"/>
        <stop offset="0.4" stop-color="#e8233f"/>
        <stop offset="1" stop-color="#ff4b63"/>
      </linearGradient>
      <linearGradient id="button-fill" x1="0" x2="1">
        <stop offset="0" stop-color="var(--btn-yellow)"/>
        <stop offset="1" stop-color="var(--btn-orange)"/>
      </linearGradient>
      <linearGradient id="product-fill" x1="0" y1="0" x2="1" y2="1">
        <stop offset="0" stop-color="#262626"/>
        <stop offset="0.45" stop-color="#e8324e"/>
        <stop offset="0.75" stop-color="#1f2a66"/>
        <stop offset="1" stop-color="#3ac9d4"/>
      </linearGradient>
      <filter id="card-shadow" x="-10%" y="-10%" width="120%" height="120%">
        <feDropShadow dx="0" dy="6" stdDeviation="8" flood-color="#000" flood-opacity="0.25"/>
      </filter>
    </defs>

    <!-- card frame -->
    <rect class="card-frame" x="75" y="175" width="1050" height="1150" rx="80" fill="var(--card-red)" filter="url(#card-shadow)"/>
    <rect x="80" y="180" width="1040" height="1140" rx="76" fill="none" stroke="var(--card-rim)" stroke-width="6"/>

    <!-- dark panel with diagonal bands -->
    <rect class="card-panel" x="118" y="218" width="962" height="1062" rx="36" fill="var(--panel-dark)"/>
    <polygon class="band-top" points="118,380 600,218 1045,218 1080,240 1080,240 118,565" fill="var(--card-red)"/>
    <polygon class="band-right" points="955,460 1080,415 1080,770 1055,775" fill="var(--card-red)"/>
    <polygon class="band-left" points="118,820 205,785 300,1105 400,1280 118,1280" fill="var(--card-red)"/>
    <polygon class="band-bottom" points="290,1105 1080,1015 1080,1070 600,1280 400,1280" fill="var(--card-red)"/>

    <!-- rarity ribbon -->
    <polygon class="rarity-ribbon" points="90,318 360,318 420,373 360,428 90,428" fill="url(#ribbon-fill)"/>
    <polyline points="348,325 405,373 348,421" fill="none" stroke="#2b1a1a" stroke-width="4"/>
    <circle cx="180" cy="375" r="28" fill="none" stroke="var(--white)" stroke-width="5"/>

    <!-- rank pill -->
    <rect class="rank-pill" x="735" y="262" width="250" height="50" rx="18" fill="#d6203c"/>
    <circle cx="853" cy="287" r="16" fill="var(--chip-blue)" stroke="#c9e0ff" stroke-width="3"/>
    <circle cx="893" cy="287" r="16" fill="var(--chip-blue)" stroke="#c9e0ff" stroke-width="3"/>
    <circle cx="933" cy="287" r="16" fill="var(--chip-blue)" stroke="#c9e0ff" stroke-width="3"/>

    <!-- timer -->
    <circle class="timer-ring" cx="980" cy="330" r="72" fill="none" stroke="var(--ring-orange)" stroke-width="5"/>
    <circle cx="980" cy="330" r="62" fill="none" stroke="#c81e36" stroke-width="14"/>
    <circle cx="980" cy="338" r="45" fill="var(--white)"/>
    <rect x="978" y="205" width="38" height="50" rx="6" fill="#c81e36"/>
    <circle class="timer-badge" cx="993" cy="290" r="38" fill="#d6203c" stroke="#a8122a" stroke-width="4"/>

    <!-- product image -->
    <rect class="product-frame" x="332" y="495" width="574" height="523" fill="none" stroke="var(--white)" stroke-width="5"/>
    <rect class="product-image" x="336" y="499" width="566" height="515" fill="url(#product-fill)" opacity="0.85" role="img" aria-label="Illustration of a red, navy and turquoise running sneaker with loose red laces"/>

    <!-- price -->
    <rect class="price-box" x="505" y="1088" width="187" height="95" rx="16" fill="var(--price-grey)"/>
    <g class="coin-stack" fill="#e3b224" stroke="#9c7410" stroke-width="2">
      <ellipse cx="548" cy="1152" rx="26" ry="9"/>
      <ellipse cx="548" cy="1140" rx="26" ry="9"/>
      <ellipse cx="548" cy="1128" rx="26" ry="9"/>
      <ellipse cx="548" cy="1116" rx="26" ry="9"/>
    </g>

    <!-- view button -->
    <rect class="view-button" x="472" y="1172" width="253" height="66" rx="24" fill="url(#button-fill)"/>
  </svg>

  <span class="rarity-label">Epic</span>
  <span class="rank-label">Very Rare</span>
  <span class="timer-label">10H</span>
  <h1 class="product-name">Boombox Master</h1>
  <span class="price-value">3,100</span>
  <span class="view-label">View</span>
</main>
</body>
</html>
```